Clothing Brand E-Commerce Website Design

We would like you to provide an ecommerce design template in layered PSD for our clothing/fashion brand website called "FernQuill".
We want the site to have a simple but sleek design similar to the following sites:
http://www.threadorbit.example/
http://tovalenwick.example/
http://www.sadiplume.example/
We want it to look stunning and blow the example sites out of the water. For color scheme, please use your imagination and try to impress us with your creativity.
We like teal and beige pink, with teal dominant.
Teal #7AFFFF / #46C6C6
Beige/pink #FF7B7C / #C74646
We want you to develop the design for 3 pages:
1) Home Page
Samples:
http://www.threadorbit.example/
http://tovalenwick.example/
http://www.sadiplume.example/
2) Products List Page (e.g., lists all "Dresses" when category is selected)
http://www.threadorbit.example/shop/casual-dresses
http://www.sadiplume.example/index.php?main_page=index&cPath=3
http://tovalenwick.example/modest-dresses.html
http://www.lunahive88.example/Product/Category.aspx?br=lh8&category=dress_maxi
3) Product Detail Page (e.g., individual product page with "Add to Cart")
http://www.threadorbit.example/shop/dresses/willow-dawn-dress
http://tovalenwick.example/modest-dresses/modest-dress-opal.html
http://www.sadiplume.example/index.php?main_page=product_info&cPath=3&products_id=297
Industry/Entity Type
Fashion

```html
<!DOCTYPE html>
<html lang="en">
<head>
<meta charset="utf-8">
<title>FernQuill – Women Dresses</title>
<link href="https://fonts.googleapis.com/css2?family=Lato:wght@300;400;700&display=swap" rel="stylesheet">
<style>
:root{
  --teal:#2fb3b3;
  --teal-dark:#1f8f8f;
  --teal-soft:#bfe6e6;
  --teal-wash:#eef8f8;
  --ink:#333;
  --muted:#8a8a8a;
  --line:#dcdcdc;
  --bg:#fff;
  --band:#f2f3f2;
}
*{box-sizing:border-box;margin:0;padding:0}
html,body{width:1200px;height:2761px;overflow:hidden;background:var(--bg)}
body{position:relative;font-family:"Lato",Arial,sans-serif;color:var(--ink)}
a{color:inherit;text-decoration:none}
ul{list-style:none}
.abs{position:absolute}

.edge-strip{position:absolute;left:0;width:1200px;height:14px;background:linear-gradient(90deg,#f4c7c8,#cfe9ea,#f6e2b8,#d7d0ee,#f4c7c8,#cfe9ea,#f6e2b8)}
.edge-strip.top{top:0}
.edge-strip.bottom{bottom:0}

/* header */
.phone{left:96px;top:80px;font-size:17px;font-weight:700;color:var(--teal-dark);display:flex;align-items:center;gap:8px}
.brand{left:488px;top:50px;display:flex;align-items:center;gap:12px;font-size:28px;font-weight:700;color:var(--teal-dark)}
.brand-dot{width:22px;height:22px;border-radius:50%;background:var(--teal-dark)}
.account{left:800px;top:84px;font-size:12px;color:#666}
.search{left:935px;top:77px;width:170px;height:33px;border:1.5px solid var(--teal);display:flex;align-items:center;justify-content:space-between;padding:0 8px;font-size:11px;color:#999}

.main-nav{left:0;top:147px;width:1200px;height:50px;border-top:1px solid var(--line);border-bottom:1px solid var(--line)}
.main-nav span{position:absolute;top:17px;font-size:12.5px;letter-spacing:.3px;color:#444}
.main-nav .caret::after{content:"";display:inline-block;width:5px;height:5px;border-right:1px solid #999;border-bottom:1px solid #999;transform:rotate(45deg);margin-left:9px;position:relative;top:-3px}
.nav-divider{left:964px;top:0;width:1px;height:48px;background:var(--line)}
.cart{font-weight:400}
.cart b{color:var(--teal);font-size:20px;font-weight:400;position:relative;top:2px}

/* sidebar */
.sidebar{left:101px;top:218px;width:172px}
.side-title{font-size:13px;font-weight:700;letter-spacing:.3px;padding-bottom:6px;border-bottom:1px dashed var(--line)}
.cat-main{font-size:14px;color:#333;margin-top:10px}
.sub-cats li{font-size:12px;color:#777;line-height:23px;padding-left:0;margin-left:0}
.sub-cats{margin:4px 0 6px 0}
.top-cats li{font-size:14px;color:var(--teal-dark);line-height:25.3px}
.refine{margin-top:14px}
.refine-label{font-size:12px;color:var(--muted);margin-top:4px;padding-bottom:6px;border-bottom:1px dashed var(--line)}
.swatches{display:grid;grid-template-columns:repeat(4,26px);gap:11px 11px;margin:12px 0 0 10px}
.swatches i{width:26px;height:26px;border-radius:50%;display:block}
.price-label{font-size:12px;color:var(--muted);margin-top:24px;padding-bottom:6px;border-bottom:1px dashed var(--line)}
.slider{position:relative;height:60px;margin-top:14px}
.slider .track{position:absolute;left:18px;right:20px;top:30px;height:12px;border-radius:6px;background:var(--teal)}
.slider .tag{position:absolute;top:6px;font-size:9px;background:#eee;border:1px solid #ccc;padding:2px 5px;color:#555}
.promo{left:103px;top:1023px;width:169px;height:306px;border:3px solid #4fd0b8;background:repeating-linear-gradient(135deg,#f7f9fb 0 8px,#eef2f6 8px 16px);text-align:center;color:var(--teal)}
.promo .p1{margin-top:22px;font-size:13px;font-weight:700;letter-spacing:1px;line-height:19px}
.promo .big{font-size:64px;font-weight:300;line-height:66px;margin-top:10px}
.promo .p2{margin-top:60px;font-size:13px;font-weight:700;letter-spacing:1px;line-height:19px}

/* hero */
.hero{left:298px;top:219px;width:813px;height:315px;background:linear-gradient(90deg,#e9eef0,#f3f6f6 50%,#e9eef0)}
.hero-photo{position:absolute;top:0;height:315px}
.hero-photo.left{left:50px;width:190px;background:linear-gradient(180deg,#cfd6d8,#3fb6c7 45%,#2a8da0)}
.hero-photo.right{right:30px;width:130px;background:linear-gradient(180deg,#d8d2d2,#8e2f3e 40%,#6e1f2e)}
.hero-copy{position:absolute;left:245px;top:60px;width:330px;text-align:right}
.hero-copy .s{font-size:36px;font-weight:300;color:#444;letter-spacing:1px;line-height:36px}
.hero-copy .c{font-size:48px;font-weight:400;color:var(--teal);line-height:46px}
.hero-copy .y{font-size:96px;font-weight:700;color:#333;line-height:90px;letter-spacing:-2px}
.hero-copy .shop{font-size:24px;font-weight:700;color:var(--teal);line-height:24px}

/* listing */
.list-bar{left:298px;top:574px;width:813px;height:22px;border-bottom:1px solid var(--line);font-size:11px}
.list-bar .title{position:absolute;left:0;top:0;font-weight:700;font-size:13px}
.list-bar .title small{color:var(--muted);font-weight:400;font-size:11px;margin-left:4px}
.list-bar .pager{position:absolute;right:10px;top:2px;color:#666}
.list-bar .pager .t{color:var(--teal)}

.grid{left:298px;top:620px;width:813px;display:grid;grid-template-columns:repeat(3,250px);column-gap:31px;row-gap:112px}
.card{position:relative;height:300px}
.card .photo{height:300px;width:100%}
.badge-new{position:absolute;top:48px;left:28px;width:86px;height:86px;border-radius:50%;background:rgba(140,208,208,.65);color:#333;font-size:15px;display:flex;align-items:center;justify-content:center;letter-spacing:.5px}
.badge-new.right{left:auto;right:28px}
.card .meta{position:absolute;top:312px;left:0;width:100%;padding-bottom:8px;border-bottom:1px solid var(--line)}
.buy{display:inline-block;background:#888;color:#fff;font-size:9px;font-weight:700;padding:3px 8px}
.price{position:absolute;right:10px;top:0;font-size:24px;font-weight:700;color:#444}
.maker{font-size:12px;color:#777;margin-top:8px}
.name{font-size:11px;color:#999;margin-top:4px}

.back-bar{left:298px;top:2278px;width:813px;height:30px;background:var(--teal-wash);font-size:12px;color:var(--teal-dark);display:flex;align-items:center;padding-left:12px;gap:8px}
.sort{position:absolute;right:0;top:4px;width:150px;height:22px;border:1px solid var(--teal-soft);background:#fff;font-size:10px;color:#777;padding:4px 8px}
.sort b{color:#333;font-weight:400}

/* newsletter */
.news-band{left:0;top:2333px;width:1200px;height:100px;background:var(--band)}
.free-circle{left:112px;top:2306px;width:154px;height:154px;border-radius:50%;background:var(--teal-soft);text-align:center;color:#174f4f;padding-top:26px}
.free-circle .f{font-size:27px;line-height:28px}
.free-circle .s{font-size:19px;line-height:22px}
.free-circle .m{font-size:28px;line-height:32px}
.news-text{left:288px;top:2358px;font-size:19px;line-height:26px;color:#444}
.news-input{left:746px;top:2361px;width:360px;height:44px;border:1.5px solid var(--teal);border-radius:8px;background:#fff;font-size:11px;color:#999;padding:14px 16px}
.news-input .go{position:absolute;right:-1px;top:-1px;width:46px;height:44px;border-left:1.5px solid var(--teal);display:flex;align-items:center;justify-content:center}

/* footer */
.foot-col{top:2500px;width:170px}
.foot-col h4{font-size:16px;font-weight:400;color:#444;padding-bottom:10px;border-bottom:1px solid var(--line)}
.foot-col li{font-size:12px;color:#777;line-height:27px;padding-left:16px;position:relative}
.foot-col li::before{content:"";position:absolute;left:2px;top:11px;width:4px;height:4px;border-right:1px solid var(--teal);border-bottom:1px solid var(--teal);transform:rotate(-45deg)}
.contact li{padding-left:26px}
.contact li::before{display:none}
.contact svg{position:absolute;left:2px;top:7px}
.socials{display:flex;gap:10px;margin:8px 0 0 18px}
.socials i{width:22px;height:22px;border-radius:50%;border:1px solid #ccc;display:block}
.foot-rule{left:112px;top:2696px;width:996px;height:1px;background:var(--line)}
.copyright{left:117px;top:2716px;font-size:11px;color:#999}
.legal{left:838px;top:2716px;font-size:11px;color:#999}
</style>
</head>
<body>
<div class="edge-strip top" role="img" aria-label="Decorative pastel pattern strip"></div>

<header>
  <div class="abs phone">
    <svg width="16" height="16" viewBox="0 0 16 16"><circle cx="8" cy="8" r="7" fill="none" stroke="#1f8f8f" stroke-width="1.5"/><path d="M5.5 4.5l1.5 0 .6 2-1 .8a5 5 0 002.2 2.2l.8-1 2 .6 0 1.5c-3.5.4-6.5-2.6-6.1-6.1z" fill="#1f8f8f"/></svg>
    1800-555-0142
  </div>
  <a class="abs brand" href="#"><span class="brand-dot"></span>FernQuill</a>
  <div class="abs account">Register &nbsp;·&nbsp; Log In ⌄</div>
  <div class="abs search">Search ...
    <svg width="14" height="14" viewBox="0 0 14 14"><circle cx="6" cy="6" r="4.5" fill="none" stroke="#2fb3b3" stroke-width="1.5"/><path d="M9.5 9.5l3.5 3.5" stroke="#2fb3b3" stroke-width="1.5"/></svg>
  </div>
  <nav class="abs main-nav">
    <span style="left:101px">HOME</span>
    <span class="caret" style="left:190px">ORDERING</span>
    <span class="caret" style="left:322px">SHIPPING</span>
    <span class="caret" style="left:453px">FASHION CLOTHES</span>
    <span class="caret" style="left:620px">STYLISTA INSIDER.</span>
    <span class="caret" style="left:789px">COLLECTIONS</span>
    <i class="abs nav-divider"></i>
    <span class="cart" style="left:986px;top:13px">SHOPPING <b>(0)</b></span>
  </nav>
</header>

<aside class="abs sidebar">
  <div class="side-title">CLOTHING</div>
  <div class="cat-main">Dresses</div>
  <ul class="sub-cats">
    <li>Party</li><li>Special Occasion</li><li>Casual</li><li>Prints</li><li>Solids</li><li>Floral</li><li>Fit &amp; Flare</li><li>Strapless</li><li>Longer Lengths</li>
  </ul>
  <ul class="top-cats">
    <li>Maxi</li><li>Tops</li><li>Bottoms</li><li>Outerwear</li><li>Swimwear</li><li>Tights &amp; Socks</li><li>Intimates</li><li>Plus Sizes</li>
  </ul>
  <div class="side-title refine" style="border:0;padding:0">REFINE BY:</div>
  <div class="refine-label">Color</div>
  <div class="swatches">
    <i style="background:#e03a3a"></i><i style="background:#f08a2e"></i><i style="background:#f5c42a"></i><i style="background:#5cbf5a"></i>
    <i style="background:#4a78d8"></i><i style="background:#9a7ad6"></i><i style="background:#ef8fb0"></i><i style="background:#9b6b45"></i>
    <i style="background:#333"></i><i style="background:#aaa"></i><i style="background:#fff;border:1px solid #ccc"></i><i style="background:linear-gradient(135deg,#f5e9c9,#c8a95c)"></i>
  </div>
  <div class="price-label">Select Price</div>
  <div class="slider">
    <span class="tag" style="left:4px">£100</span>
    <span class="tag" style="right:4px">£900</span>
    <span class="track"></span>
  </div>
</aside>

<div class="abs promo">
  <div class="p1">MUST-HAVES<br>NOW ON SALE</div>
  <div class="big">30%<br>OFF</div>
  <div class="p2">SHOP WHILE<br>THEY LAST</div>
</div>

<section class="abs hero">
  <div class="hero-photo left" role="img" aria-label="Model in a turquoise printed summer dress"></div>
  <div class="hero-copy">
    <div class="s">SUMMER</div>
    <div class="c">COLLECTION</div>
    <div class="y">2014</div>
    <div class="shop">SHOP NOW</div>
  </div>
  <div class="hero-photo right" role="img" aria-label="Model in a burgundy sleeveless dress"></div>
</section>

<div class="abs list-bar">
  <div class="title">WOMEN DRESSES <small>3662 Products</small></div>
  <div class="pager">items 1 - 300 of 3415 &nbsp; <span class="t">Show 50</span> &nbsp;|&nbsp; <span class="t">Showing</span> &nbsp;&nbsp; Prev &nbsp;<span class="t">1</span>&nbsp; <span class="t">2</span> &nbsp;<span class="t">3...</span> &nbsp;&nbsp;&nbsp;&nbsp; <span class="t">12</span> &nbsp;&nbsp; <span class="t">Next</span></div>
</div>

<main class="abs grid">
  <article class="card"><div class="photo" role="img" aria-label="Model in a pink floral print sundress" style="background:linear-gradient(180deg,#f3f3f3,#e6b7c6 55%,#d994a8)"></div><div class="meta"><span class="buy">BUY</span><span class="price">$64.52</span><div class="maker">Lirra Mode</div><div class="name">Red Lace Bodycon Long Dress</div></div></article>
  <article class="card"><div class="photo" role="img" aria-label="Model in a long pink maxi dress with chevron hem" style="background:linear-gradient(180deg,#f3f3f3,#f06a8e 50%,#e2507a)"></div><span class="badge-new">NEW</span><div class="meta"><span class="buy">BUY</span><span class="price">$64.52</span><div class="maker">Lirra Mode</div><div class="name">Red Lace Bodycon Long Dress</div></div></article>
  <article class="card"><div class="photo" role="img" aria-label="Model in a coral polka dot dress" style="background:linear-gradient(180deg,#f3f3f3,#ec7f87 55%,#d9616d)"></div><div class="meta"><span class="buy">BUY</span><span class="price">$64.52</span><div class="maker">Lirra Mode</div><div class="name">Red Lace Bodycon Long Dress</div></div></article>

  <article class="card"><div class="photo" role="img" aria-label="Model in a yellow floral dress" style="background:linear-gradient(180deg,#f3f3f3,#f4c76a 55%,#eeaf45)"></div><span class="badge-new">NEW</span><div class="meta"><span class="buy">BUY</span><span class="price">$64.52</span><div class="maker">Lirra Mode</div><div class="name">Red Lace Bodycon Long Dress</div></div></article>
  <article class="card"><div class="photo" role="img" aria-label="Model in a red lace dress" style="background:linear-gradient(180deg,#f3f3f3,#e0303a 45%,#c91f2a)"></div><div class="meta"><span class="price">$64.52</span><div class="maker" style="margin-top:26px">Lirra Mode</div><div class="name">Red Lace Bodycon Long Dress</div></div></article>
  <article class="card"><div class="photo" role="img" aria-label="Model in a black polka dot halter dress" style="background:linear-gradient(180deg,#f3f3f3,#3a3a3a 50%,#222)"></div><span class="badge-new">NEW</span><div class="meta"><span class="buy">BUY</span><span class="price">$64.52</span><div class="maker">Lirra Mode</div><div class="name">Red Lace Bodycon Long Dress</div></div></article>

  <article class="card"><div class="photo" role="img" aria-label="Model in a black and white striped dress" style="background:linear-gradient(180deg,#f3f3f3,#9a9a9a 55%,#6e6e6e)"></div><div class="meta"><span class="buy">BUY</span><span class="price">$64.52</span><div class="maker">Lirra Mode</div><div class="name">Red Lace Bodycon Long Dress</div></div></article>
  <article class="card"><div class="photo" role="img" aria-label="Model in a pink and white striped dress" style="background:linear-gradient(180deg,#f3f3f3,#f29ac3 55%,#e880b0)"></div><span class="badge-new">NEW</span><div class="meta"><span class="price">$64.52</span><div class="maker" style="margin-top:26px">Lirra Mode</div><div class="name">Red Lace Bodycon Long Dress</div></div></article>
  <article class="card"><div class="photo" role="img" aria-label="Model in a pale floral print dress" style="background:linear-gradient(180deg,#f3f3f3,#dcdbe6 55%,#b7b6cc)"></div><div class="meta"><span class="buy">BUY</span><span class="price">$64.52</span><div class="maker">Lirra Mode</div><div class="name">Red Lace Bodycon Long Dress</div></div></article>

  <article class="card"><div class="photo" role="img" aria-label="Model in a long sleeve teal dress" style="background:linear-gradient(180deg,#f5f5f5,#3bb89a 50%,#2aa585)"></div><span class="badge-new right">NEW</span><div class="meta"><span class="buy">BUY</span><span class="price">$64.52</span><div class="maker">Lirra Mode</div><div class="name">Red Lace Bodycon Long Dress</div></div></article>
  <article class="card"><div class="photo" role="img" aria-label="Model in an orange and blue print shift dress" style="background:linear-gradient(180deg,#f3f3f3,#e8502a 45%,#2d4d9c)"></div><div class="meta"><span class="price">$64.52</span><div class="maker" style="margin-top:26px">Lirra Mode</div><div class="name">Red Lace Bodycon Long Dress</div></div></article>
  <article class="card"><div class="photo" role="img" aria-label="Model in a pale pink embroidered dress" style="background:linear-gradient(180deg,#f5f5f5,#f1d8de 50%,#e7c0ca)"></div><span class="badge-new">NEW</span><div class="meta"><span class="buy">BUY</span><span class="price">$64.52</span><div class="maker">Lirra Mode</div><div class="name">Red Lace Bodycon Long Dress</div></div></article>
</main>

<div class="abs back-bar">
  <svg width="10" height="8" viewBox="0 0 10 8"><path d="M1 7l4-5 4 5" fill="none" stroke="#1f8f8f" stroke-width="1.5"/></svg>
  Back to Top
  <div class="sort">Sort By: <b>Popularity</b> <span style="float:right;color:#2fb3b3">⌄</span></div>
</div>

<section>
  <div class="abs news-band"></div>
  <div class="abs free-circle"><div class="f">FREE</div><div class="s">Shipping<br>Order Over</div><div class="m">$100</div></div>
  <p class="abs news-text">Sign Up For Our Newsletter &amp; Receive Special Offer<br>and Discounts.</p>
  <div class="abs news-input">Enter your email address here
    <span class="go"><svg width="14" height="14" viewBox="0 0 14 14"><path d="M4 2v7h7M8 6l3 3-3 3" fill="none" stroke="#2fb3b3" stroke-width="1.5"/></svg></span>
  </div>
</section>

<footer>
  <div class="abs foot-col" style="left:112px"><h4>About FernQuill</h4><ul><li>Our Blog</li><li>About Our Shop</li><li>Secure Shopping</li><li>Privacy Policy</li></ul></div>
  <div class="abs foot-col" style="left:315px"><h4>Experience</h4><ul><li>Shipping Rates</li><li>Order Status</li><li>Contact Us</li><li>Testimonials</li></ul></div>
  <div class="abs foot-col" style="left:524px"><h4>Guarantee</h4><ul><li>30 Day Returns</li><li>Return Instructions</li><li>Secure Shopping</li><li>Repairs After Warranty</li></ul></div>
  <div class="abs foot-col" style="left:736px"><h4>More</h4><ul><li>Customer Support</li><li>FAQ</li><li>Gift Cards</li><li>Follow Us</li></ul></div>
  <div class="abs foot-col contact" style="left:942px"><h4>Contact Us</h4>
    <ul>
      <li><svg width="12" height="12" viewBox="0 0 12 12"><path d="M2 1.5h2l1 2.5-1.3 1a6 6 0 002.8 2.8l1-1.3 2.5 1v2C6 10 2 6 2 1.5z" fill="#2fb3b3"/></svg>+49 89 555 0101 0</li>
      <li><svg width="12" height="12" viewBox="0 0 12 12"><rect x="1" y="3" width="10" height="7" fill="none" stroke="#2fb3b3" stroke-width="1.3"/><path d="M1 3l5 4 5-4" fill="none" stroke="#2fb3b3" stroke-width="1.3"/></svg>info@fernquill.example</li>
      <li style="line-height:16px;padding-top:5px"><svg width="12" height="14" viewBox="0 0 12 14"><path d="M6 13s4.5-5 4.5-8A4.5 4.5 0 001.5 5c0 3 4.5 8 4.5 8z" fill="#2fb3b3"/><circle cx="6" cy="5" r="1.6" fill="#fff"/></svg>main streeet 123 block<br>main road</li>
    </ul>
    <div class="socials"><i></i><i></i><i></i><i></i></div>
  </div>
  <div class="abs foot-rule"></div>
  <div class="abs copyright">All content and images Copyright © FernQuill.example 2014. All rights reserved.</div>
  <div class="abs legal">Site Map &nbsp;·&nbsp; Privacy Policy &nbsp;·&nbsp; Terms &amp; Conditions</div>
</footer>

<div class="edge-strip bottom" role="img" aria-label="Decorative pastel pattern strip"></div>
</body>
</html>
```